Tove & Lark Designs - Promotions flyer

I am a locally based Interior designer /stylist on Sydney's lower north shore. I would like to offer my services:
Full Professional Styling Services and Furniture Hire
Colour Consultation – Interior / exterior
Floor Coverings
Furniture selection and sourcing
Window Treatments
Wallpaper
Soft Furnishings
Upholstery
Renovations

I would like to offer a free consultation
Updates

Project Deadline Extended
Reason: I've been speaking with a designer and need her to make one more change. I have tried to message her twice, but have had no reply. Once she makes these changes I'm ready to sign off on the design. Thanks Harriet

Target Market(s)

30 - 60's middle to high income earners

Industry/Entity Type

Floor

Requirements
Must have
• one sided DL size
Use my logo
1 or 2 images of interior space or image of a lamp, cushion, lounge etc
The following contact details:
Mobile: 041 xxx xxxx
Website Address: www.tovelarkdesigns.example.au

```html
<!DOCTYPE html>
<html lang="en">
<head>
<meta charset="utf-8">
<title>Tove &amp; Lark Designs – DL Flyer</title>
<link href="https://fonts.googleapis.com/css2?family=Oswald:wght@300;400;600&family=Righteous&display=swap" rel="stylesheet">
<style>
  :root{
    --backdrop:#3b241a;
    --paper-top:#a9a9ab;
    --paper-mid:#e6e6e6;
    --paper-bottom:#f1efe9;
    --orange:#f0682c;
    --ink:#111111;
    --grey-text:#8a8a8a;
    --badge-grey:#6d6d6d;
    --frame:#000000;
    --photo-light:#e9ece6;
    --photo-green:#a8c23c;
  }
  *{margin:0;padding:0;box-sizing:border-box}
  html,body{width:1200px;height:1053px;overflow:hidden}
  body{background:var(--backdrop);position:relative;font-family:'Oswald',sans-serif}

  .flyer{
    position:absolute;left:361px;top:20px;width:478px;height:1013px;overflow:hidden;
    background:linear-gradient(180deg,var(--paper-top) 0%,var(--paper-mid) 42%,var(--paper-bottom) 100%);
  }

  .hero{position:absolute;left:0;top:0;width:478px;height:480px}

  .headline{
    position:absolute;left:30px;top:326px;width:180px;text-align:center;
    font-family:'Righteous',sans-serif;font-size:36px;line-height:46px;
    color:var(--orange);text-transform:uppercase;letter-spacing:1px;
  }

  .services-title{
    position:absolute;left:204px;top:474px;width:258px;text-align:center;
    font-weight:600;font-size:26px;line-height:33px;color:var(--ink);
  }
  .services-list{
    position:absolute;left:190px;top:620px;width:286px;text-align:center;list-style:none;
    font-weight:300;font-size:20px;line-height:24.8px;color:var(--grey-text);
  }

  .offer-badge{position:absolute;left:50px;top:718px;width:150px;height:150px}

  .brand-name{
    position:absolute;left:130px;top:870px;width:260px;text-align:center;
    font-weight:400;font-size:34px;line-height:40px;color:var(--orange);
  }
  .contact{
    position:absolute;left:110px;width:300px;text-align:center;color:var(--orange);
  }
  .contact-mobile{top:966px;font-weight:600;font-size:15px;line-height:18px}
  .contact-web{top:985px;font-weight:400;font-size:12px;line-height:15px}
</style>
</head>
<body>
  <main class="flyer">
    <svg class="hero" viewBox="0 0 478 480">
      <defs>
        <linearGradient id="photo-tones" x1="0" y1="0" x2="1" y2="1">
          <stop offset="0" stop-color="#f4f5f1"/>
          <stop offset="0.4" stop-color="#d8ddd6"/>
          <stop offset="0.62" stop-color="#a8c23c"/>
          <stop offset="0.8" stop-color="#cfd3cc"/>
          <stop offset="1" stop-color="#eef0ea"/>
        </linearGradient>
      </defs>
      <polygon class="hero-frame" points="70,-60 43,140 232,458 452,330" fill="var(--frame)"/>
      <polygon class="hero-photo" role="img" aria-label="Photograph of a styled living room: white bookshelves, a lime green armchair with cushion and a hammock by a bright window"
        points="302,-41 93,83 248,429 457,305" fill="url(#photo-tones)"/>
    </svg>

    <h1 class="headline">We<br>take<br>space<br>and<br>make<br>it<br>your<br>place!</h1>

    <h2 class="services-title">Full Professional<br>Styling Services<br>and<br>Furniture Hire</h2>
    <ul class="services-list">
      <li>Colour Consultation</li>
      <li>Interior/exterior</li>
      <li>Floor Coverings</li>
      <li>Furniture selection and sourcing</li>
      <li>Window Treatments</li>
      <li>Wallpaper</li>
      <li>Soft Furnishings</li>
      <li>Upholstery</li>
      <li>Renovations</li>
    </ul>

    <svg class="offer-badge" viewBox="0 0 150 150" aria-label="Free consultation">
      <defs>
        <path id="arc-top" d="M 22 75 A 53 53 0 0 1 128 75"/>
        <path id="arc-bottom" d="M 13 75 A 62 62 0 0 0 137 75"/>
      </defs>
      <circle cx="75" cy="75" r="73" fill="#ffffff"/>
      <circle cx="75" cy="75" r="68" fill="var(--orange)"/>
      <circle cx="75" cy="75" r="44" fill="var(--badge-grey)" stroke="#ffffff" stroke-width="2"/>
      <text font-family="Oswald, sans-serif" font-weight="600" font-size="14" fill="#ffffff" letter-spacing="2">
        <textPath href="#arc-top" startOffset="50%" text-anchor="middle">FREE</textPath>
      </text>
      <text font-family="Oswald, sans-serif" font-weight="600" font-size="13" fill="#ffffff" letter-spacing="1">
        <textPath href="#arc-bottom" startOffset="50%" text-anchor="middle">CONSULTATION</textPath>
      </text>
      <text x="75" y="72" text-anchor="middle" font-family="Oswald, sans-serif" font-weight="400" font-size="17" fill="var(--orange)">Tove &amp;</text>
      <text x="75" y="92" text-anchor="middle" font-family="Oswald, sans-serif" font-weight="400" font-size="17" fill="var(--orange)">Lark</text>
    </svg>

    <p class="brand-name">Tove &amp; Lark<br>Designs</p>
    <p class="contact contact-mobile">Mobile: 041 xxx xxxx</p>
    <p class="contact contact-web">www.tovelarkdesigns.example.au</p>
  </main>
</body>
</html>
```